Korvatch Law Rebrand

I am recreating my law firm website. I got a new logo and would like to recreate the website to match the new logo. the website is korvatchlaw.com

```html
<!DOCTYPE html>
<html lang="en">
<head>
<meta charset="utf-8">
<title>Korvatch Law, PLLC</title>
<link rel="stylesheet" href="https://fonts.googleapis.com/css2?family=Montserrat:wght@500;600;700;800&family=Arimo:wght@400;700&display=swap">
<style>
:root{
  --navy:#0b4f91;
  --navy-deep:#084581;
  --slate:#8d9cbd;
  --slate-light:#a9b5cf;
  --ink:#1c1c1c;
  --body:#2b2b2b;
  --white:#ffffff;
  --mist:#e6eaf2;
}
*{box-sizing:border-box;margin:0;padding:0}
html,body{width:1200px;height:4286px;overflow:hidden}
body{position:relative;background:var(--white);font-family:"Arimo",Arial,sans-serif;color:var(--body)}
.abs{position:absolute}

/* top bar */
.topbar{left:0;top:0;width:1200px;height:38px;background:var(--slate)}
.topbar__call,.topbar__cta{top:0;height:38px;display:flex;align-items:center;gap:8px;color:var(--white);font:600 14px "Montserrat",Arial,sans-serif;white-space:nowrap}
.topbar__call{left:104px}
.topbar__cta{right:104px}
.topbar__tab{left:520px;top:0;width:160px;height:38px}

/* header */
.header{left:0;top:38px;width:1200px;height:95px;background:var(--white)}
.nav a{position:absolute;top:50px;font:600 14px "Montserrat",Arial,sans-serif;color:var(--ink);text-decoration:none;letter-spacing:.2px;white-space:nowrap}
.nav a.is-active{color:var(--navy)}
.brand{left:480px;top:82px;width:240px;text-align:center;font:700 20px "Montserrat",Arial,sans-serif;letter-spacing:3px;color:var(--navy);white-space:nowrap}
.brand__sub{display:block;font-size:10px;letter-spacing:3px;margin-top:1px}

/* hero */
.hero{left:0;top:133px;width:1200px;height:524px;background:linear-gradient(180deg,#c3c9d2 0%,#dfe2e6 40%,#b9c0c9 75%,#8e97a3 100%)}
.hero__title{left:0;top:290px;width:1200px;text-align:center;color:var(--white);font:800 33px/40px "Montserrat",Arial,sans-serif}
.btn{display:inline-flex;align-items:center;justify-content:center;gap:8px;border-radius:24px;font:700 15px "Montserrat",Arial,sans-serif;color:var(--white);text-decoration:none;white-space:nowrap}
.btn--solid{background:var(--navy);border:2px solid #2f6fb0}
.btn--outline{border:2px solid var(--white);color:var(--white)}
.hero__btn{left:449px;top:397px;width:302px;height:44px}

/* welcome */
.welcome{left:0;top:657px;width:1200px;height:628px;background:linear-gradient(180deg,#ffffff 0%,#f1f3f7 55%,#dde2ec 100%)}
.welcome__title{left:128px;top:108px;font:800 38px/46px "Montserrat",Arial,sans-serif;color:var(--navy);white-space:nowrap}
.welcome__title span{color:var(--slate)}
.welcome__text{left:128px;top:222px;width:478px;font-size:14px;line-height:18px;color:var(--ink)}
.welcome__text p{margin-bottom:19px}
.welcome__btn{left:128px;top:495px;width:176px;height:46px}

/* section headings */
.section-title{left:0;width:1200px;text-align:center;font:800 42px "Montserrat",Arial,sans-serif;color:var(--navy)}
.section-title span{color:var(--slate)}
.section-rule{left:484px;width:232px;height:3px;background:var(--slate)}

/* practice cards */
.card{width:443px;height:431px;background:var(--white);box-shadow:0 2px 12px rgba(0,0,0,.12)}
.card__photo{position:absolute;left:0;top:0;width:443px;height:226px;clip-path:polygon(0 0,100% 0,100% 85%,0 100%)}
.card__title{position:absolute;left:30px;top:252px;font:600 25px "Montserrat",Arial,sans-serif;color:var(--ink);white-space:nowrap}
.card__text{position:absolute;left:31px;top:308px;width:360px;font-size:14px;line-height:21px;color:var(--ink)}
.practice__btn{left:449px;top:2439px;width:302px;height:44px}

/* attorney */
.attorney{left:0;top:2538px;width:1200px;height:590px}
.attorney__name{left:125px;top:2678px;font:800 44px/51px "Montserrat",Arial,sans-serif;color:var(--white)}
.attorney__text{left:127px;top:2797px;width:420px;font-size:14px;line-height:18px;color:var(--white)}
.attorney__text p{margin-bottom:18px}
.attorney__btn{left:128px;top:3017px;width:176px;height:46px}
.attorney__photo{left:625px;top:2598px;width:525px;height:530px;background:linear-gradient(180deg,#5d7394 0%,#34476a 50%,#22324d 100%)}

/* blog */
.blog-feature{left:126px;top:3323px;width:426px;height:345px;background:var(--white);box-shadow:0 2px 12px rgba(0,0,0,.12)}
.blog-feature__photo{position:absolute;left:0;top:0;width:426px;height:172px;background:linear-gradient(135deg,#6b5848,#c9c3ba 55%,#8a7a6a)}
.blog-feature__title{position:absolute;left:34px;top:207px;font:600 22px "Montserrat",Arial,sans-serif;color:var(--ink)}
.blog-feature__text{position:absolute;left:34px;top:253px;width:330px;font-size:14px;line-height:20px;color:var(--ink)}
.post{left:586px;width:490px;height:143px}
.post__photo{position:absolute;left:0;top:0;width:198px;height:143px;border-radius:4px}
.post__title{position:absolute;left:223px;top:14px;font:600 18px/21px "Montserrat",Arial,sans-serif;color:var(--ink);white-space:nowrap}
.post__text{position:absolute;left:225px;top:68px;width:240px;font-size:13.5px;line-height:20px;color:var(--ink)}
.post-rule{left:809px;top:3496px;width:240px;height:1px;background:#d8dce4}

/* footer */
.footer{left:0;top:3810px;width:1200px;height:476px}
.footer__brand{left:116px;top:4004px;width:278px;text-align:center;color:var(--white);font:600 25px "Montserrat",Arial,sans-serif;letter-spacing:3px;white-space:nowrap}
.footer__brand small{display:block;font-size:13px;letter-spacing:3px;margin-top:2px}
.footer__heading{font:700 21px "Montserrat",Arial,sans-serif;color:var(--white)}
.footer__rule{height:2px;width:178px;background:var(--white)}
.footer__links a{position:absolute;left:0;color:var(--white);text-decoration:none;font:500 15px "Montserrat",Arial,sans-serif}
.footer__contact{display:flex;gap:12px;color:var(--white);font:500 15px/18px "Montserrat",Arial,sans-serif;white-space:nowrap}
.footer__copy{left:0;top:4220px;width:1200px;text-align:center;color:var(--white);font:500 14px "Montserrat",Arial,sans-serif}
</style>
</head>
<body>

<!-- top bar -->
<div class="abs topbar"></div>
<svg class="abs topbar__tab" viewBox="0 0 160 38" aria-hidden="true"><polygon points="0,0 160,0 140,38 20,38" fill="#fff"/></svg>
<div class="abs topbar__call">
  <svg width="14" height="14" viewBox="0 0 24 24" fill="#fff"><rect x="1" y="1" width="22" height="22" rx="4"/><path d="M8 6c1 3 4 8 10 11l1.5-2-3-1.5-1.2 1.2c-2-1-3.5-2.5-4.5-4.5L12 9 10.5 6z" fill="#8d9cbd"/></svg>
  CALL: (555) 014-2270
</div>
<div class="abs topbar__cta">
  SCHEDULE A CONSULTATION
  <svg width="15" height="15" viewBox="0 0 24 24" fill="none" stroke="#fff" stroke-width="2"><circle cx="12" cy="12" r="10"/><path d="M8 12h8M13 8l4 4-4 4"/></svg>
</div>

<!-- header -->
<header class="abs header">
  <nav class="nav">
    <a class="is-active" style="left:106px">HOME</a>
    <a style="left:194px">PRACTICES AREAS</a>
    <a style="left:380px">ABOUT ME</a>
    <a style="left:742px">CLIENT REVIEWS</a>
    <a style="left:912px">BLOG</a>
    <a style="left:996px">CONTACT US</a>
  </nav>
</header>
<div class="abs brand">KORVATCH LAW<span class="brand__sub">PLLC</span></div>

<!-- hero -->
<section class="abs hero" role="img" aria-label="Upward view of glass skyscrapers against a cloudy sky"></section>
<h1 class="abs hero__title">PERSONAL LEGAL SOLUTIONS IN<br>LIFE'S MOST DIFFICULT MOMENTS</h1>
<a class="abs btn btn--solid hero__btn">SCHEDULE A CONSULTATION</a>

<!-- welcome -->
<section class="abs welcome">
  <h2 class="abs welcome__title">WELCOME TO<br><span>KORVATCH LAW, PLLC</span></h2>
  <div class="abs welcome__text">
    <p>It is my honor to provide quality legal services at a reasonable price to clients that I enjoy working with and for. I am grateful for all my clients and the trust they place in me to represent them.</p>
    <p>My practice focuses on Probate, Adult Guardianships, and Trust Administration and Litigation. I also represent clients in other general civil litigation matters.&nbsp; Finally, I handle estate planning for families of modest means.</p>
    <p>As your attorney, I would educate you about the law as it pertains to your situation, guide you through your options, and then help you to achieve your desired objectives from those options.</p>
    <p>Schedule your consultation today.</p>
  </div>
  <a class="abs btn btn--solid welcome__btn">READ MORE
    <svg width="16" height="16" viewBox="0 0 24 24"><circle cx="12" cy="12" r="11" fill="#fff"/><path d="M8 12h7M12 8l4 4-4 4" stroke="#0b4f91" stroke-width="2.5" fill="none"/></svg>
  </a>
</section>

<!-- practice areas -->
<h2 class="abs section-title" style="top:1356px">PRACTICE <span>AREAS</span></h2>
<div class="abs section-rule" style="top:1421px"></div>

<article class="abs card" style="left:135px;top:1474px">
  <div class="card__photo" role="img" aria-label="Row of leather-bound law books on a shelf" style="background:linear-gradient(90deg,#5a2a1c,#a35a3c 40%,#7a3a26 70%,#c9a68a)"></div>
  <h3 class="card__title">Probate and Trusts</h3>
  <p class="card__text">Guiding clients through the legal process of administering a deceased person's estate, ensuring that assets are distributed according to their wishes while addressing any legal complexities that may arise.</p>
</article>
<article class="abs card" style="left:619px;top:1474px">
  <div class="card__photo" role="img" aria-label="Hand signing a document beside a small model house" style="background:linear-gradient(135deg,#e9e6e2,#f7f5f2 50%,#d8c9b6)"></div>
  <h3 class="card__title">Estate Planning</h3>
  <p class="card__text">Helping individuals and families create tailored plans that safeguard their assets, ensure their wishes are fulfilled, and provide for their loved ones after they pass away.</p>
</article>
<article class="abs card" style="left:135px;top:1947px">
  <div class="card__photo" role="img" aria-label="Elderly hands held together in comfort" style="background:linear-gradient(135deg,#3e4a3c,#8a7a6c 50%,#2f3a30)"></div>
  <h3 class="card__title" style="left:36px">Adult Guardianships</h3>
  <p class="card__text">Assisting families in securing legal guardianship for individuals who are unable to make decisions for themselves, ensuring that their rights and well-being are protected through compassionate and effective representation.</p>
</article>
<article class="abs card" style="left:619px;top:1947px">
  <div class="card__photo" role="img" aria-label="Lawyer writing on papers next to a judge's gavel" style="background:linear-gradient(135deg,#4a3020,#b08a6a 50%,#e2d8cc)"></div>
  <h3 class="card__title">Civil Litigation</h3>
  <p class="card__text">Representing clients in legal disputes, advocating for their rights and interests in various matters such as contract disputes, personal injury claims, and property issues, with a focus on achieving favorable outcomes through negotiation or trial.</p>
</article>

<a class="abs btn btn--solid practice__btn">SCHEDULE A CONSULTATION</a>

<!-- attorney -->
<svg class="abs attorney" viewBox="0 0 1200 590" preserveAspectRatio="none" aria-hidden="true">
  <polygon points="0,0 1200,95 1200,590 0,590" fill="#0b4f91"/>
  <polygon points="520,50 1200,95 1200,150 700,100" fill="#1a5c9c" opacity=".6"/>
</svg>
<h2 class="abs attorney__name">ADRIAN<br>KORVATCH</h2>
<div class="abs attorney__text">
  <p>I am Adrian Korvatch and I am Korvatch Law PLLC. I started this firm to provide quality legal services at a reasonable price to those in need.</p>
  <p>My practice focuses on Probate, Adult Guardianships, and Trust Administration and Litigation. I represent clients in other general civil litigation matters as well as in emergency mental health situations. Finally, I handle estate planning for families of modest means because I truly believe that all would benefit from an estate plan.</p>
</div>
<a class="abs btn btn--outline attorney__btn">READ MORE
  <svg width="16" height="16" viewBox="0 0 24 24"><circle cx="12" cy="12" r="11" fill="#fff"/><path d="M8 12h7M12 8l4 4-4 4" stroke="#0b4f91" stroke-width="2.5" fill="none"/></svg>
</a>
<div class="abs attorney__photo" role="img" aria-label="Portrait photo of the attorney"></div>

<!-- blog -->
<h2 class="abs section-title" style="top:3211px">LATEST <span>BLOG POSTS</span></h2>
<div class="abs section-rule" style="top:3278px"></div>

<article class="abs blog-feature">
  <div class="blog-feature__photo" role="img" aria-label="Hands reviewing and signing a document on a clipboard"></div>
  <h3 class="blog-feature__title">Trusts vs. Wills</h3>
  <p class="blog-feature__text">When it comes to estate planning, two of the most common tools are trusts and wills. While both serve essential purposes</p>
</article>

<article class="abs post" style="top:3323px">
  <div class="post__photo" role="img" aria-label="Library shelves filled with law books" style="background:linear-gradient(135deg,#7a2a22,#3a4a5a 50%,#8a3a2a)"></div>
  <h3 class="post__title">Why probate is needed,...<br>sometimes</h3>
  <p class="post__text">Lorem ipsum dolor sit amet, conse ctetur adipiscing elit, sed do eiusm od tempor incididunt.</p>
</article>
<div class="abs post-rule"></div>
<article class="abs post" style="top:3523px">
  <div class="post__photo" role="img" aria-label="People discussing documents at a desk" style="background:linear-gradient(135deg,#c98a5a,#e8e4de 50%,#9ab0c8)"></div>
  <h3 class="post__title">Estate Planning<br>Essentials</h3>
  <p class="post__text">Lorem ipsum dolor sit amet, conse ctetur adipiscing elit, sed do eiusm od tempor incididunt.</p>
</article>

<!-- footer -->
<svg class="abs footer" viewBox="0 0 1200 476" preserveAspectRatio="none" aria-hidden="true">
  <polygon points="0,45 1200,0 1200,476 0,476" fill="#0b4f91"/>
</svg>
<div class="abs footer__brand">KORVATCH LAW<small>PLLC</small></div>

<div class="abs footer__heading" style="left:528px;top:3896px">Links</div>
<div class="abs footer__rule" style="left:528px;top:3936px"></div>
<div class="abs footer__links" style="left:535px;top:3962px;width:200px;height:170px">
  <a style="top:0">Home</a>
  <a style="top:36px">About Us</a>
  <a style="top:72px">Practice Area</a>
  <a style="top:109px">Blog</a>
  <a style="top:145px">Contact</a>
</div>

<div class="abs footer__heading" style="left:822px;top:3896px">Contact</div>
<div class="abs footer__rule" style="left:822px;top:3936px"></div>
<div class="abs footer__contact" style="left:822px;top:3962px">
  <svg width="15" height="15" viewBox="0 0 24 24" fill="#fff"><rect x="1" y="1" width="22" height="22" rx="4"/><path d="M8 6c1 3 4 8 10 11l1.5-2-3-1.5-1.2 1.2c-2-1-3.5-2.5-4.5-4.5L12 9 10.5 6z" fill="#0b4f91"/></svg>
  <span>(555) 014-2270</span>
</div>
<div class="abs footer__contact" style="left:822px;top:3998px">
  <svg width="15" height="18" viewBox="0 0 24 30" fill="#fff"><path d="M12 0a10 10 0 0 0-10 10c0 8 10 20 10 20s10-12 10-20A10 10 0 0 0 12 0zm0 14a4 4 0 1 1 0-8 4 4 0 0 1 0 8z"/></svg>
  <span>240 Maple Avenue Suite B<br>Riverton, Texas 77000</span>
</div>
<div class="abs footer__contact" style="left:822px;top:4054px">
  <svg width="15" height="15" viewBox="0 0 24 24"><circle cx="12" cy="12" r="11" fill="#fff"/><path d="M12 6v6l4 3" stroke="#0b4f91" stroke-width="2.5" fill="none"/></svg>
  <span>Mon - Fri&nbsp; 8AM - 5PM</span>
</div>

<div class="abs footer__copy">© 2025 Korvatch Law, PLLC | All Rights Reserved</div>

</body>
</html>
```